serious, thorough, light and simple - that's my advice and mediations

My business card should combine my logo (uploaded file) and my homepage (https://feltra-mediation.plavosite.com).

Contact Information for Business Card

Name: Sabine Feltra di Olvesi
Phone: 079 417 68 92
mail: sfeltra@plovix.ch
web: www.feltra-di-olvesi.ch

```html
<!DOCTYPE html>
<html lang="de">
<head>
<meta charset="utf-8">
<title>Visitenkarte – Sabine Feltra di Olvesi</title>
<link rel="stylesheet" href="https://fonts.googleapis.com/css2?family=Montserrat:wght@300;400&family=Roboto+Condensed:wght@400&display=swap">
<style>
  :root {
    --backdrop: #4b4e52;
    --card: #ffffff;
    --brand-blue: #1f3f95;
    --brand-green: #1d6b45;
    --brand-gold: #b08a4e;
    --card-shadow: rgba(0, 0, 0, 0.35);
  }
  * { box-sizing: border-box; margin: 0; padding: 0; }
  html, body {
    width: 1200px;
    height: 965px;
    overflow: hidden;
    background: var(--backdrop);
    font-family: "Montserrat", sans-serif;
  }
  .card {
    position: absolute;
    width: 620px;
    height: 360px;
    background: var(--card);
    box-shadow: 0 8px 24px var(--card-shadow);
    overflow: hidden;
  }
  .card--front { left: 40px; top: 60px; }
  .card--back { left: 540px; top: 520px; }

  .front-band {
    position: absolute;
    left: 0; top: 0; bottom: 0;
    width: 190px;
    background: linear-gradient(160deg, var(--brand-green), var(--brand-blue));
    clip-path: polygon(0 0, 100% 0, 45% 100%, 0 100%);
  }
  .brand {
    position: absolute;
    display: flex;
    align-items: center;
    gap: 16px;
    color: var(--brand-gold);
    font-family: "Montserrat", sans-serif;
    font-weight: 400;
    white-space: nowrap;
  }
  .brand__dot {
    border-radius: 50%;
    background: var(--brand-green);
    flex: none;
  }
  .card--front .brand { left: 160px; top: 150px; font-size: 42px; }
  .card--front .brand__dot { width: 32px; height: 32px; }
  .card--back .brand { left: 40px; top: 150px; font-size: 32px; }
  .card--back .brand__dot { width: 24px; height: 24px; }

  .holder-name {
    position: absolute;
    right: 40px;
    top: 56px;
    font-family: "Roboto Condensed", sans-serif;
    font-weight: 400;
    font-size: 30px;
    color: var(--brand-blue);
  }
  .contact-list {
    position: absolute;
    right: 40px;
    bottom: 44px;
    list-style: none;
    display: flex;
    flex-direction: column;
    gap: 8px;
  }
  .contact-list li {
    display: flex;
    align-items: center;
    gap: 10px;
    font-size: 17px;
    font-weight: 400;
    color: var(--brand-gold);
  }
  .contact-list svg {
    width: 17px;
    height: 17px;
    flex: none;
    stroke: var(--brand-blue);
    fill: none;
    stroke-width: 1.6;
    stroke-linecap: round;
    stroke-linejoin: round;
  }
</style>
</head>
<body>
  <section class="card card--front" aria-label="Vorderseite">
    <div class="front-band"></div>
    <div class="brand"><span class="brand__dot"></span>Leute im Wandel</div>
  </section>

  <section class="card card--back" aria-label="Rückseite">
    <h1 class="holder-name">Sabine Feltra di Olvesi</h1>
    <div class="brand"><span class="brand__dot"></span>Leute im Wandel</div>
    <ul class="contact-list">
      <li>
        <svg viewBox="0 0 16 16" aria-hidden="true"><path d="M4 2l2.5 3-1.5 1.5a8 8 0 0 0 4.5 4.5L11 9.5l3 2.5-1.5 2C7 14 2 9 2 3.5z"/></svg>
        079 417 68 92
      </li>
      <li>
        <svg viewBox="0 0 16 16" aria-hidden="true"><rect x="1.5" y="3.5" width="13" height="9"/><path d="M1.5 3.5L8 9l6.5-5.5"/></svg>
        sfeltra@plovix.ch
      </li>
      <li>
        <svg viewBox="0 0 16 16" aria-hidden="true"><circle cx="8" cy="8" r="6.5"/><path d="M1.5 8h13M8 1.5c-2.5 3-2.5 10 0 13M8 1.5c2.5 3 2.5 10 0 13"/></svg>
        www.feltra-di-olvesi.ch
      </li>
    </ul>
  </section>
</body>
</html>
```